Brindle Hub is an online marketing platform

A daily deals site for consumers a way to bring in new clients for clients and this is who the business cards are for. Industries - Food and Drink, Things To Do, Beauty and Spas, Staycations and Services.This leaflet is going to be used to get member of the public to sign up to our website

```html
<!DOCTYPE html>
<html lang="en">
<head>
<meta charset="utf-8">
<title>Brindle Hub – Launch Leaflet</title>
<link rel="stylesheet" href="https://fonts.googleapis.com/css2?family=Archivo+Black&family=Roboto:wght@400;700;900&display=swap">
<style>
  :root {
    --page-bg: #e4e6ea;
    --navy: #0f1b3d;
    --navy-deep: #0a1230;
    --brand-blue: #1d5fae;
    --bright-blue: #1f8fd0;
    --band-blue: #1c7fc4;
    --black: #0b0b0d;
    --white: #ffffff;
    --ink: #111111;
  }
  * { box-sizing: border-box; margin: 0; padding: 0; }
  html, body { width: 1120px; height: 1200px; overflow: hidden; }
  body {
    background: var(--page-bg);
    font-family: "Roboto", Arial, sans-serif;
    position: relative;
  }
  .leaflet {
    position: absolute;
    left: 148px; top: 20px;
    width: 824px; height: 1160px;
    background: var(--white);
    overflow: hidden;
    box-shadow: 0 6px 24px rgba(0,0,0,.18);
  }
  .abs { position: absolute; }

  .photo-restaurant {
    left: 0; top: 238px; width: 824px; height: 364px;
    background: linear-gradient(180deg, #c9b9a8 0%, #8a7565 28%, #4a3b33 55%, #1d2a44 80%, #15203a 100%);
  }
  .photo-cycling {
    left: 0; top: 816px; width: 824px; height: 301px;
    background: linear-gradient(180deg, #e9ecea 0%, #c9d1c6 35%, #8fa36c 65%, #4e6a2c 100%);
  }

  .shapes { left: 0; top: 0; width: 824px; height: 1160px; pointer-events: none; }

  .brand-name {
    left: 330px; top: 62px; width: 340px; text-align: center;
    font-weight: 900; font-size: 52px; color: var(--brand-blue);
    line-height: 1;
  }

  .prize-band {
    left: 0; top: 602px; width: 824px; height: 108px;
    background: var(--black);
  }
  .prize-text {
    left: 150px; top: 618px; width: 660px;
    color: var(--white); font-weight: 700; font-size: 25px;
    line-height: 1.35; text-align: center;
  }

  .intro-band {
    left: 0; top: 710px; width: 824px; height: 106px;
    background: var(--band-blue);
  }
  .intro-text {
    left: 20px; top: 728px; width: 784px;
    color: var(--white); font-weight: 400; font-size: 20.5px;
    line-height: 1.4; text-align: center;
  }

  .launch-title {
    left: 22px; top: 828px;
    font-family: "Archivo Black", "Arial Black", sans-serif;
    font-size: 42px; color: var(--ink); line-height: 1;
  }
  .launch-date {
    left: 72px; top: 884px;
    font-family: "Archivo Black", "Arial Black", sans-serif;
    font-size: 30px; color: var(--ink); line-height: 1;
  }
  .offer-line {
    left: 60px; top: 964px; width: 660px;
    color: var(--white); font-weight: 700; font-size: 33px; white-space: nowrap;
  }
  .win-word {
    left: 300px; top: 1008px;
    color: var(--white); font-weight: 900; font-size: 96px; line-height: 1;
  }
  .follow-label {
    left: 660px; top: 1024px; width: 150px; text-align: center;
    color: var(--white); font-weight: 700; font-size: 18px;
  }
  .social-row {
    left: 610px; top: 1055px;
    display: flex; gap: 10px;
  }
  .social-dot {
    width: 56px; height: 56px; border-radius: 50%;
    background: var(--navy-deep); border: 3px solid var(--white);
  }

  .footer-band {
    left: 0; top: 1117px; width: 824px; height: 43px;
    background: var(--navy-deep);
  }
  .footer-text {
    left: 0; top: 1124px; width: 824px; text-align: center;
    color: var(--white); font-weight: 700; font-size: 24px;
  }
</style>
</head>
<body>
  <main class="leaflet">
    <div class="abs photo-restaurant" role="img" aria-label="Photo of an elegant restaurant dining room with tables, blue booth seating and large windows overlooking the countryside at sunset"></div>
    <div class="abs photo-cycling" role="img" aria-label="Photo of mountain bikers riding along a grassy hillside trail under a pale sky"></div>

    <svg class="abs shapes" viewBox="0 0 824 1160" aria-hidden="true">
      <polygon points="0,0 150,0 0,230" fill="var(--navy)"/>
      <polygon points="150,0 235,0 0,330 0,230" fill="var(--bright-blue)"/>
      <polygon points="824,25 824,238 500,238" fill="var(--bright-blue)"/>
      <polygon points="824,140 824,340 690,238" fill="var(--navy)"/>
      <polygon points="0,330 0,420 70,238 40,238" fill="var(--navy)"/>
      <polygon points="0,470 0,602 95,602" fill="var(--navy)"/>
      <polygon points="760,602 824,520 824,602" fill="var(--navy)"/>
      <polygon points="0,816 60,816 0,880" fill="var(--navy)"/>
      <polygon points="720,816 824,816 824,1000" fill="var(--bright-blue)"/>
      <polygon points="780,816 824,816 824,900" fill="var(--navy)"/>
      <polygon points="0,1060 0,1117 60,1117" fill="var(--navy)"/>
    </svg>

    <div class="abs brand-name">Brindle Hub</div>

    <div class="abs prize-band"></div>
    <p class="abs prize-text">Hey You ! Want to win £200 to spend on the best experiences the South West has to offer ?</p>

    <div class="abs intro-band"></div>
    <p class="abs intro-text">Brindle Hub is s brand spanking new website that gives you access to exciting offers across the best restaurants,hotels,spas leisure activities and services.</p>

    <h1 class="abs launch-title">Launching on the</h1>
    <p class="abs launch-date">1ST AUGUST 2019</p>
    <p class="abs offer-line">Be the first to receive exclusive offers and</p>
    <p class="abs win-word">win!</p>

    <p class="abs follow-label">follow us on</p>
    <div class="abs social-row" aria-label="Social media links">
      <span class="social-dot"></span>
      <span class="social-dot"></span>
      <span class="social-dot"></span>
    </div>

    <div class="abs footer-band"></div>
    <p class="abs footer-text">Register for free @ brindlehub.co.uk</p>
  </main>
</body>
</html>
```